Brochure Design Project

We are a payroll company. We offer a wide variety of products and services:
1. Payroll Processing
2. Employee Direct Deposit
3. Time and attendance
4. HR services
5. Employee Employee Benefits

I'd like to develop a one page template that uses a combination of our logo (attached), colors (attached) and possible a picture. The picture could be shown as an option as it may change based on the product or service.

Target Market(s)

Adults in the United States ages 22-50. Typically these people are accountants, human resource professionals or entrepreneurs. The payroll industry is dominated by 3 large payroll processors, QLM, Wendrafy and Tolvarex. These companies are very impersonal and make it difficult to resolve issues when they arise. We have grown to over 400 clients by being the opposite of the big guys,

Industry/Entity Type

It Company

Font styles to use
Sans Serif

Requirements
Must have
• The brochure can be one or two pages.
Nice to have
• I'll know it when I see it but I can't describe it. I have attached a few brochures that have caught my eye.
Should not have
• No cartoons. No money signs. Hip, new, fresh are words I'd use to describe the winning product. Of the three people I described in my target market, the entrepreneur is the market I'd most like to target.

```html
<!DOCTYPE html>
<html lang="en">
<head>
<meta charset="utf-8">
<title>Paystead Partners – Two Page Brochure</title>
<link href="https://fonts.googleapis.com/css2?family=PT+Sans:wght@400;700&family=PT+Sans+Narrow:wght@400;700&display=swap" rel="stylesheet">
<style>
:root{
  --navy:#23305f;
  --green:#b3cc55;
  --ink:#4a4a4c;
  --body:#555559;
  --grey-head:#9a9a9e;
  --panel-top:#e6e7ef;
  --panel-bottom:#f6f6fa;
  --page-top:#e8e9f1;
  --page:#ffffff;
  --backdrop:#f4f1e6;
  --band-navy:rgba(35,48,95,.22);
  --band-green:rgba(179,204,85,.35);
}
*{margin:0;padding:0;box-sizing:border-box}
html,body{width:1200px;height:1000px;overflow:hidden;background:var(--backdrop)}
.spread{position:relative;width:1200px;height:1000px}
.page{position:absolute;top:145px;width:565px;height:710px;background:linear-gradient(180deg,var(--page-top) 0%,var(--page) 45%);overflow:hidden;font-family:"PT Sans",sans-serif;color:var(--body)}
.page--front{left:27px}
.page--back{left:607px}
.header-band{position:absolute;left:0;width:565px}
.header-band--front{top:48px;height:112px;background:linear-gradient(180deg,transparent 0%,var(--band-navy) 40%,var(--band-green) 75%,transparent 100%)}
.header-band--back{top:40px;height:84px;background:linear-gradient(180deg,transparent 0%,var(--band-green) 35%,var(--band-navy) 65%,transparent 100%)}
.brand{position:absolute;font-family:"PT Sans",sans-serif;font-weight:700;color:var(--navy);font-size:27px;line-height:26px;text-align:center}
.contact{position:absolute;font-family:"PT Sans Narrow",sans-serif;font-size:8px;line-height:11px;color:var(--navy);text-align:center}
.headline{position:absolute;font-family:"PT Sans Narrow",sans-serif;font-weight:700;font-size:33px;line-height:31px;color:var(--ink);letter-spacing:-.3px}
.headline--green{color:var(--green)}
.headline .muted{color:var(--grey-head)}
.subhead{position:absolute;font-family:"PT Sans Narrow",sans-serif;font-size:12.5px;line-height:17px;color:var(--ink)}
.lead{font-family:"PT Sans Narrow",sans-serif;font-weight:700;font-size:6.9px;line-height:11.5px;letter-spacing:-.1px;color:var(--ink)}
.lead--blue{color:#6a6f93}
.panel{position:absolute;background:linear-gradient(180deg,var(--panel-top),var(--panel-bottom))}
.item{position:absolute;width:236px}
.item h3{font-family:"PT Sans Narrow",sans-serif;font-weight:700;font-size:8.5px;color:var(--green);margin-bottom:4px}
.item p{font-size:9.2px;line-height:14.3px;letter-spacing:-.1px;text-align:justify}
.tabs{position:absolute;left:17px;top:656px;width:530px;height:38px;display:flex;gap:2px}
.tabs li{list-style:none;flex:1;background:linear-gradient(180deg,#f1f1f6,#e3e4ec);border-bottom:3px solid #cfd0d8;font-size:8px;color:var(--navy);display:flex;align-items:center;justify-content:center;text-transform:uppercase}
.service-nav{position:absolute;left:18px;top:195px;font-size:7.2px;color:var(--navy);text-transform:uppercase;white-space:nowrap}
.service-nav span{padding:0 3px}
.chart-note{position:absolute;left:307px;top:257px;width:82px;font-family:"PT Sans Narrow",sans-serif;font-weight:700;font-size:4.6px;line-height:6px;color:var(--navy);text-align:right}
.pie{position:absolute;left:400px;top:228px;width:128px;height:70px}
.photo{position:absolute;left:221px;top:556px;width:320px;height:128px;background:linear-gradient(90deg,#eef0f2 0%,#d9d6d2 45%,#c9b8a6 65%,#e9e8e6 100%)}
</style>
</head>
<body>
<div class="spread">

  <section class="page page--front">
    <div class="header-band header-band--front" role="img" aria-label="Decorative navy and green header band"></div>
    <div class="brand" style="left:360px;top:30px;width:170px">Paystead<br>Partners</div>
    <div class="contact" style="left:340px;top:91px;width:210px">http://www.paysteadco.com/<br>Ph: 555-014-2290 | E-mail: hello@paysteadco.com</div>

    <h1 class="headline" style="left:20px;top:178px">LOREM IPSUM<br>DOLOR SIT AMET</h1>
    <div class="subhead" style="left:20px;top:240px">PHASELLUS RHONCUS TINCIDUNT TELLUS,<br>A VESTIBULUM NISI FEUGIAT EGET</div>
    <p class="lead" style="position:absolute;left:20px;top:280px;width:262px">LOREM IPSUM DOLOR SIT AMET, CONSECTETUR ADIPISCING ELIT. MAURIS ALIQUA NUNC SED VELIT FRINGILLA VIVERRA. VESTIBULUM NON LIGULA SED NISL SCELERI PORTTITOR VITAE IN LIGULA. VIVAMUS LAOREET, METUS A ADIPISCING EUISMOD,</p>

    <div class="panel" style="left:20px;top:325px;width:261px;height:318px"></div>
    <div class="panel" style="left:285px;top:180px;width:262px;height:463px"></div>

    <p class="chart-note">LOREM IPSUM DOLOR SIT AMET. CONSECTETUR ADIPISCING ELIT. NULLA COMMODO DUI EGET LIGULA SEMPER ET ORNARE IN TINCIDUNT. CLASS APTENT TACITI SOCIOSQU AD LITORA PER CONUBIA NOSTRA.</p>
    <svg class="pie" viewBox="0 0 128 70" aria-label="Pie chart" role="img">
      <defs><linearGradient id="pieSide" x1="0" x2="1"><stop offset="0" stop-color="#cfd0d4"/><stop offset="1" stop-color="#b9babf"/></linearGradient></defs>
      <path d="M8,26 L8,42 A60,20 0 0 0 128,42 L128,26 Z" fill="url(#pieSide)"/>
      <ellipse cx="68" cy="26" rx="60" ry="20" fill="#eeeff2"/>
      <path d="M60,34 L44,54 A56,16 0 0 1 16,46 L16,40 Z" fill="#1b5fa8"/>
      <path d="M60,30 L46,48 A56,16 0 0 1 16,40 Z" fill="#2c78c8"/>
      <path d="M60,28 L18,36 A60,20 0 0 1 26,20 Z" fill="#fff" opacity=".7"/>
    </svg>

    <div class="item" style="left:33px;top:346px"><h3>NULLAM VEHICULA JUSTO VOLUTPAT</h3><p>Etiam in elit enim. Nam pharetra, metus eget tempor aliquam, nulla felis congue purus, sit amet suscipit libero odio quis lectus. Proin lacinia dictum erat ac mattis. Mauris tincidunt interdum rhoncus.</p></div>
    <div class="item" style="left:33px;top:445px"><h3>NULLAM VEHICULA JUSTO VOLUTPAT</h3><p>Etiam in elit enim. Nam pharetra, metus eget tempor aliquam, nulla felis congue purus, sit amet suscipit libero odio quis lectus. Proin lacinia dictum erat ac mattis. Mauris tincidunt interdum rhoncus.</p></div>
    <div class="item" style="left:33px;top:544px"><h3>NULLAM VEHICULA JUSTO VOLUTPAT</h3><p>Etiam in elit enim. Nam pharetra, metus eget tempor aliquam, nulla felis congue purus, sit amet suscipit libero odio quis lectus. Proin lacinia dictum erat ac mattis. Mauris tincidunt interdum rhoncus.</p></div>
    <div class="item" style="left:299px;top:346px"><h3>NULLAM VEHICULA JUSTO VOLUTPAT</h3><p>Etiam in elit enim. Nam pharetra, metus eget tempor aliquam, nulla felis congue purus, sit amet suscipit libero odio quis lectus. Proin lacinia dictum erat ac mattis. Mauris tincidunt interdum rhoncus.</p></div>
    <div class="item" style="left:299px;top:445px"><h3>NULLAM VEHICULA JUSTO VOLUTPAT</h3><p>Etiam in elit enim. Nam pharetra, metus eget tempor aliquam, nulla felis congue purus, sit amet suscipit libero odio quis lectus. Proin lacinia dictum erat ac mattis. Mauris tincidunt interdum rhoncus.</p></div>
    <div class="item" style="left:299px;top:544px"><h3>NULLAM VEHICULA JUSTO VOLUTPAT</h3><p>Etiam in elit enim. Nam pharetra, metus eget tempor aliquam, nulla felis congue purus, sit amet suscipit libero odio quis lectus. Proin lacinia dictum erat ac mattis. Mauris tincidunt interdum rhoncus.</p></div>

    <ul class="tabs">
      <li>Payroll Processing</li><li>Employee Direct Deposit</li><li>Time and Attendance</li><li>HR Servicesemployee</li><li>Employee Benefits</li>
    </ul>
  </section>

  <section class="page page--back">
    <div class="header-band header-band--back" role="img" aria-label="Decorative green and navy header band"></div>

    <h1 class="headline headline--green" style="left:18px;top:129px">LOREM IPSUM<br>DOLOR SIT AMET <span class="muted">DOLOR SIT</span></h1>
    <nav class="service-nav"><span>Payroll Processing</span>|<span>Employee Direct Deposit</span>|<span>Time and Attendance</span>|<span>HR Servicesemployee</span>|<span>Employee Benefits</span></nav>

    <div class="panel" style="left:18px;top:216px;width:261px;height:320px"></div>
    <div class="panel" style="left:284px;top:216px;width:262px;height:320px"></div>

    <div class="item" style="left:31px;top:258px"><h3>NULLAM VEHICULA JUSTO VOLUTPAT</h3><p>Etiam in elit enim. Nam pharetra, metus eget tempor aliquam, nulla felis congue purus, sit amet suscipit libero odio quis lectus. Proin lacinia dictum erat ac mattis. Mauris tincidunt interdum rhoncus.</p></div>
    <div class="item" style="left:31px;top:357px"><h3>NULLAM VEHICULA JUSTO VOLUTPAT</h3><p>Etiam in elit enim. Nam pharetra, metus eget tempor aliquam, nulla felis congue purus, sit amet suscipit libero odio quis lectus. Proin lacinia dictum erat ac mattis. Mauris tincidunt interdum rhoncus.</p></div>
    <div class="item" style="left:31px;top:458px"><h3>NULLAM VEHICULA JUSTO VOLUTPAT</h3><p>Etiam in elit enim. Nam pharetra, metus eget tempor aliquam, nulla felis congue purus, sit amet suscipit libero odio quis lectus. Proin lacinia dictum erat ac mattis. Mauris tincidunt interdum rhoncus.</p></div>

    <p class="lead lead--blue" style="position:absolute;left:298px;top:262px;width:236px">LOREM IPSUM DOLOR SIT AMET, CONSECTETUR ADIPISCING ELIT. MAURIS ALIQUA NUNC SED VELIT FRINGILLA VIVERRA. VESTIBULUM NON LIGULA SED NISL SCELERI PORTTITOR VITAE IN LIGULA. VIVAMUS LAOREET, METUS A ADIPISCING EUISMOD,</p>
    <p class="lead lead--blue" style="position:absolute;left:298px;top:307px;width:236px">LOREM IPSUM DOLOR SIT AMET, CONSECTETUR ADIPISCING ELIT. MAURIS ALIQUA NUNC SED VELIT FRINGILLA VIVERRA. VESTIBULUM NON LIGULA SED NISL SCELERI PORTTITOR VITAE IN LIGULA. VIVAMUS LAOREET, METUS A ADIPISCING EUISMOD,</p>
    <div class="item" style="left:298px;top:357px"><h3>NULLAM VEHICULA JUSTO VOLUTPAT</h3><p>Etiam in elit enim. Nam pharetra, metus eget tempor aliquam, nulla felis congue purus, sit amet suscipit libero odio quis lectus. Proin lacinia dictum erat ac mattis. Mauris tincidunt interdum rhoncus.</p></div>
    <div class="item" style="left:298px;top:456px"><h3>NULLAM VEHICULA JUSTO VOLUTPAT</h3><p>Etiam in elit enim. Nam pharetra, metus eget tempor aliquam, nulla felis congue purus, sit amet suscipit libero odio quis lectus. Proin lacinia dictum erat ac mattis. Mauris tincidunt interdum rhoncus.</p></div>

    <div class="brand" style="left:28px;top:603px;width:150px">Paystead<br>Partners</div>
    <div class="contact" style="left:0;top:665px;width:206px">http://www.paysteadco.com/<br>Ph: 555-014-2290 | E-mail: hello@paysteadco.com</div>

    <div class="photo" role="img" aria-label="Photo of a smiling professional woman with colleagues in a bright office meeting"></div>
  </section>

</div>
</body>
</html>
```